Business Card design which attached logo. Company is called Tailored Shield and main colours are Orange & Black.

Company specialises in Paint Protection and Detailing for supercars.

Details needed on business card:

Sales

Address: Unit 14, 227 Harlow Street, Fernmere Vale, NSW 2391

Phone: 02 8419 2753

website: www.tailoredshield.com.au

Email: sales@tailoredshield.com.au

```html
<!DOCTYPE html>
<html lang="en">
<head>
<meta charset="utf-8">
<title>Tailored Shield – Business Card</title>
<link href="https://fonts.googleapis.com/css2?family=Open+Sans:wght@300;400;600&display=swap" rel="stylesheet">
<style>
  :root {
    --backdrop: #3f3733;
    --card: #0d0d0e;
    --orange: #e8612a;
    --orange-dim: #b94c22;
    --text-light: #e6e6e6;
    --text-muted: #bdbdbd;
  }
  * { margin: 0; padding: 0; box-sizing: border-box; }
  html, body { width: 1200px; height: 716px; overflow: hidden; }
  body {
    background: var(--backdrop);
    font-family: "Open Sans", Arial, sans-serif;
    display: flex;
    align-items: center;
    justify-content: center;
    gap: 40px;
  }
  .card {
    width: 540px;
    height: 308px;
    background: var(--card);
    position: relative;
    box-shadow: 0 12px 30px rgba(0,0,0,.45);
  }
  /* Front */
  .card--front {
    display: flex;
    flex-direction: column;
    align-items: center;
    justify-content: center;
    gap: 26px;
  }
  .brand-name {
    color: var(--orange-dim);
    font-weight: 300;
    letter-spacing: 2px;
    text-transform: uppercase;
  }
  .card--front .brand-name { font-size: 30px; }
  .front-web {
    color: var(--text-muted);
    font-size: 14px;
  }
  .front-web .accent { color: var(--orange); }
  /* Back */
  .card--back { display: flex; align-items: center; }
  .back-brand {
    width: 52%;
    display: flex;
    justify-content: center;
  }
  .card--back .brand-name { font-size: 19px; }
  .divider {
    width: 2px;
    height: 150px;
    background: var(--orange);
  }
  .contact {
    padding-left: 18px;
    color: var(--text-light);
    font-size: 12.5px;
    line-height: 1.45;
  }
  .contact-company {
    color: var(--orange);
    font-size: 21px;
    line-height: 1.1;
    text-transform: uppercase;
  }
  .contact-role {
    font-size: 17px;
    font-weight: 300;
    margin-bottom: 8px;
  }
  .contact-line { display: flex; align-items: center; gap: 6px; }
  .contact-line svg { width: 11px; height: 11px; flex: none; }
  .contact-line .accent { color: var(--orange); }
</style>
</head>
<body>
  <section class="card card--front">
    <div class="brand-name">Tailored Shield</div>
    <div class="front-web">www.<span class="accent">tailoredshield</span>.com.au</div>
  </section>

  <section class="card card--back">
    <div class="back-brand">
      <div class="brand-name">Tailored Shield</div>
    </div>
    <div class="divider"></div>
    <div class="contact">
      <div class="contact-company">Tailored Shield</div>
      <div class="contact-role">Founder &amp; CEO</div>
      <div>Unit 14, 227 Harlow Street,</div>
      <div>Fernmere Vale, NSW 2391</div>
      <div class="contact-line">
        <svg viewBox="0 0 12 12"><rect x="3" y="1" width="6" height="10" rx="1" fill="none" stroke="#e8612a" stroke-width="1.3"/></svg>
        02 8419 2753
      </div>
      <div class="contact-line">
        <svg viewBox="0 0 12 12"><rect x="1" y="3" width="10" height="7" fill="none" stroke="#e8612a" stroke-width="1.3"/><path d="M1 3l5 4 5-4" fill="none" stroke="#e8612a" stroke-width="1.3"/></svg>
        sales@tailoredshield.com.au
      </div>
      <div class="contact-line">
        <svg viewBox="0 0 12 12"><circle cx="6" cy="6" r="4.8" fill="none" stroke="#e8612a" stroke-width="1.3"/><path d="M1.2 6h9.6M6 1.2c-2.4 3-2.4 6.6 0 9.6M6 1.2c2.4 3 2.4 6.6 0 9.6" fill="none" stroke="#e8612a" stroke-width="1"/></svg>
        <span>www.<span class="accent">tailoredshield</span>.com.au</span>
      </div>
    </div>
  </section>
</body>
</html>
```